I am medical doctor in surgery specialized in Urology and anti-aging. I need Web and Instagram design for a head cream , face cream and body lotion. I did a 2% GHK-Cu solution (head-face-body) with an professional pharmacist specialized in manufacturing creams. . GHK-Cu is a tri-peptide with solid scientific background to rejuvenate the skin (will stimulate collagen production) and can promote hair regrowth. Statistically 70% of peptides bought are fake on the market, I can personally guarantee about purity (my peptides are certified pure above 99% checked in an independent laboratory in London -UK.
I want to use the name 'Lunavel'. I secured already the domain names. I had an design for another project I could re-use for this project. The ribbon should include more blue. The font of Lunavel can be changed. I got a logo which is ok for me. Web design best coded with Wordpress.

Target Market(s)

Anti aging, skin care, hair regrowth, skin collagen

Industry/Entity Type

the cream can also be used after surgery for faster and better wound healing

Number of Pages Required

5+ page

Font styles to use
Sans Serif

Colors
0054AA
0677BA
7BADD7
CADEEF
E8F1F8

Requirements
Must have
• target population 30-70 years
Nice to have
• scientific proof, pictures before-after
Should not have
• GHK-Cu has solid scientific animal studies of anti-cancer properties. It is 100% safe for dermal human use.

```html
<!DOCTYPE html>
<html lang="en">
<head>
<meta charset="utf-8">
<title>Lunavel — The Collection</title>
<link href="https://fonts.googleapis.com/css2?family=Inter:wght@400;500;600;700&family=Lexend:wght@600;700;800&display=swap" rel="stylesheet">
<style>
:root{
  --blue:#0054AA;
  --blue-mid:#0677BA;
  --blue-soft:#7BADD7;
  --blue-pale:#CADEEF;
  --blue-mist:#E8F1F8;
  --navy:#0B3A7C;
  --ink:#0B2A5B;
  --text:#4A5568;
  --muted:#6B7280;
  --line:#E3EAF2;
  --white:#FFFFFF;
}
*{box-sizing:border-box;margin:0;padding:0}
html,body{width:1200px;height:2226px;overflow:hidden}
body{font-family:"Inter",sans-serif;color:var(--ink);background:var(--white);font-size:13px}
a{color:inherit;text-decoration:none}
.display{font-family:"Lexend",sans-serif}

/* top bar */
.topbar{height:31px;background:var(--navy);color:#fff;display:flex;justify-content:center;align-items:center;gap:20px;font-size:11px;font-weight:500}
.topbar span{display:flex;align-items:center;gap:6px}
.topbar svg{width:11px;height:11px}

/* nav */
.nav{height:60px;border-bottom:1px solid var(--line);display:flex;align-items:center;padding:0 50px 0 62px;position:relative}
.brand{display:flex;align-items:center;gap:8px;font-family:"Lexend",sans-serif;font-weight:700;font-size:19px;color:var(--blue-mid)}
.brand-dot{width:14px;height:14px;border-radius:50%;background:var(--blue)}
.nav-links{position:absolute;left:419px;display:flex;gap:14px;font-size:13px;font-weight:600}
.nav-links a{position:relative;color:var(--ink)}
.nav-links a.active{color:var(--blue)}
.nav-links a.active::after{content:"";position:absolute;left:50%;transform:translateX(-50%);bottom:-11px;width:22px;height:2px;background:var(--blue);border-radius:2px}
.nav-actions{margin-left:auto;display:flex;align-items:center;gap:22px}
.nav-actions svg{width:16px;height:16px;color:var(--ink)}
.btn-primary{background:var(--blue);color:#fff;font-weight:600;font-size:14px;padding:0 20px;height:41px;border-radius:21px;display:flex;align-items:center;box-shadow:0 6px 14px rgba(0,84,170,.25)}

/* hero */
.hero{height:209px;background:linear-gradient(180deg,var(--blue-mist),#fbfdff);border-bottom:1px solid var(--line);padding:57px 62px 0}
.crumbs{font-size:13.5px;color:var(--muted)}
.crumbs a{color:var(--blue)}
.crumbs i{font-style:normal;margin:0 6px}
.hero h1{font-family:"Lexend",sans-serif;font-weight:800;font-size:44px;letter-spacing:-1.5px;line-height:1;margin-top:10px;color:var(--ink)}
.hero p{font-size:14px;line-height:22px;color:var(--text);width:580px;margin-top:12px}

/* shop layout */
.shop{height:1438px;padding:44px 50px 0 62px;display:flex;gap:21px}
.filters{width:257px;height:509px;border:1px solid var(--line);border-radius:12px;padding:22px 18px}
.filters h3{font-family:"Lexend",sans-serif;font-size:12.5px;font-weight:700;color:var(--ink)}
.cat-list{list-style:none;margin-top:11px}
.cat-list li{height:34px;display:flex;align-items:center;padding-left:12px;font-size:13px;font-weight:500;color:var(--ink);margin-bottom:5px;border-radius:6px}
.cat-list li.on{background:var(--blue);color:#fff;font-weight:600}
.divider{height:1px;background:var(--line);margin:14px 0 20px}
.range{position:relative;height:6px;background:var(--line);border-radius:3px;margin:24px 0 18px}
.range::after{content:"";position:absolute;right:-1px;top:-4px;width:14px;height:14px;border-radius:50%;background:var(--blue)}
.range-labels{display:flex;justify-content:space-between;font-size:12px;color:var(--muted)}
.range-labels b{color:var(--ink)}
.filters .divider.low{margin:20px 0 14px}
.note{display:flex;gap:8px;font-size:12px;line-height:20px;color:var(--text)}
.note svg{width:12px;height:12px;flex:none;margin-top:5px}

.results{flex:1}
.results-head{height:31px;display:flex;align-items:center;justify-content:space-between;margin-bottom:21px}
.count{font-size:12.5px;color:var(--muted)}
.count b{color:var(--ink);font-weight:600}
.sort{width:139px;height:31px;border:1px solid var(--line);border-radius:7px;display:flex;align-items:center;justify-content:space-between;padding:0 8px 0 14px;font-size:12.5px;color:var(--ink)}
.sort svg{width:9px;height:9px}

.grid{display:grid;grid-template-columns:repeat(3,256px);column-gap:21px;row-gap:21px}
.card{height:402px;border:1px solid var(--line);border-radius:12px;overflow:hidden;background:#fff}
.card-media{height:255px;position:relative;background:linear-gradient(160deg,#e4eef8 0%,#f4f8fc 70%,#f8fbfe 100%)}
.pill{position:absolute;left:11px;top:11px;height:23px;padding:0 8px;border:1px solid var(--blue-pale);background:#fff;border-radius:12px;display:flex;align-items:center;gap:5px;font-size:10.5px;font-weight:600;color:var(--blue)}
.pill svg{width:10px;height:10px}
.heart{position:absolute;right:11px;top:11px;width:28px;height:28px;border-radius:8px;background:#fff;border:1px solid var(--line);display:flex;align-items:center;justify-content:center}
.heart svg{width:14px;height:14px;color:var(--ink)}
.ribbon{position:absolute;right:45px;top:13px;height:19px;padding:0 8px;border-radius:5px;background:var(--blue);color:#fff;font-size:9.5px;font-weight:700;display:flex;align-items:center}
.product-shot{position:absolute;left:50%;top:52px;transform:translateX(-50%);width:70px;height:140px;border-radius:10px;background:linear-gradient(180deg,var(--blue-soft),var(--blue-pale))}
.product-shot.jar{top:90px;width:64px;height:80px;background:linear-gradient(180deg,var(--navy) 0 18%,var(--blue-pale) 18%)}
.product-shot.deep{background:linear-gradient(180deg,var(--blue),var(--blue-mid))}
.product-shot.kit{width:100px;height:90px;top:80px;background:linear-gradient(180deg,var(--blue-pale),var(--blue-soft))}
.shadow{position:absolute;left:50%;bottom:52px;transform:translateX(-50%);width:80px;height:8px;border-radius:50%;background:rgba(11,42,91,.12)}
.card-body{padding:16px 16px 0}
.card-cat{font-size:10px;font-weight:700;letter-spacing:.9px;color:var(--blue-mid);text-transform:uppercase}
.card-name{font-family:"Lexend",sans-serif;font-weight:700;font-size:14px;color:var(--ink);margin-top:6px;letter-spacing:-.2px}
.card-desc{font-size:11.5px;line-height:18.5px;color:var(--text);margin-top:3px;height:37px}
.card-foot{display:flex;justify-content:space-between;align-items:center;margin-top:8px}
.price{font-family:"Lexend",sans-serif;font-weight:700;font-size:16px;color:var(--ink)}
.add{width:40px;height:28px;border-radius:14px;background:var(--blue);display:flex;align-items:center;justify-content:center}
.add svg{width:12px;height:12px;color:#fff}

/* trust band */
.trust{height:115px;background:var(--blue-mist);display:flex;justify-content:center;align-items:center;gap:40px;font-size:13px;font-weight:500;color:var(--text)}
.trust span{display:flex;align-items:center;gap:8px}
.trust svg{width:16px;height:16px;color:var(--blue-mid)}

/* footer */
.footer{height:373px;background:var(--navy);color:#fff;padding:62px 50px 0 62px;position:relative}
.footer-top{display:flex}
.footer-brand{width:370px}
.footer-brand .brand{color:#fff}
.footer-brand .brand-dot{background:var(--blue-soft)}
.footer-brand p{font-size:13px;line-height:20px;color:#c9d8ec;margin-top:16px;width:300px}
.lab{margin-top:22px;display:inline-flex;align-items:center;gap:7px;height:42px;padding:0 14px;border:1px solid rgba(255,255,255,.22);border-radius:9px;font-size:11.5px;color:#fff;background:rgba(255,255,255,.05)}
.lab svg{width:14px;height:14px}
.fcol{width:185px}
.fcol h4{font-family:"Lexend",sans-serif;font-size:11px;font-weight:700;letter-spacing:.5px;margin-top:-6px}
.fcol ul{list-style:none;margin-top:14px}
.fcol li{font-size:13px;color:#d4e1f2;height:30px}
.footer-bottom{position:absolute;left:62px;right:50px;top:302px;border-top:1px solid rgba(255,255,255,.16);display:flex;justify-content:space-between;align-items:center;padding-top:18px}
.footer-bottom p{font-size:11.5px;color:#c9d8ec}
.socials{display:flex;gap:8px;margin-top:-2px}
.socials span{width:34px;height:34px;border-radius:8px;border:1px solid rgba(255,255,255,.2);background:rgba(255,255,255,.06)}
</style>
</head>
<body>

<svg width="0" height="0" style="position:absolute">
  <defs>
    <symbol id="i-badge" viewBox="0 0 16 16"><circle cx="8" cy="8" r="8" fill="currentColor"/><path d="M4.6 8.2l2.2 2.1 4.6-4.6" stroke="#fff" stroke-width="1.8" fill="none" stroke-linecap="round" stroke-linejoin="round"/></symbol>
    <symbol id="i-heart" viewBox="0 0 24 24"><path d="M12 20s-7.5-4.6-7.5-10A4.2 4.2 0 0 1 12 7.3 4.2 4.2 0 0 1 19.5 10c0 5.4-7.5 10-7.5 10z" fill="none" stroke="currentColor" stroke-width="1.8" stroke-linejoin="round"/></symbol>
    <symbol id="i-bag" viewBox="0 0 24 24"><path d="M5 8h14l-1 12H6L5 8z" fill="none" stroke="currentColor" stroke-width="1.8" stroke-linejoin="round"/><path d="M9 8V6a3 3 0 0 1 6 0v2" fill="none" stroke="currentColor" stroke-width="1.8"/></symbol>
    <symbol id="i-cart" viewBox="0 0 24 24"><path d="M5 8h14l-1 12H6L5 8z" fill="none" stroke="currentColor" stroke-width="2.2" stroke-linejoin="round"/><path d="M9 8V6a3 3 0 0 1 6 0v2M12 11v6M9 14h6" fill="none" stroke="currentColor" stroke-width="2.2"/></symbol>
    <symbol id="i-shield" viewBox="0 0 24 24"><path d="M12 3l7 3v5c0 5-3.2 8.3-7 10-3.8-1.7-7-5-7-10V6l7-3z" fill="none" stroke="currentColor" stroke-width="1.8" stroke-linejoin="round"/><path d="M12 8v5M12 16v.5" stroke="currentColor" stroke-width="1.8" stroke-linecap="round"/></symbol>
    <symbol id="i-truck" viewBox="0 0 24 24"><path d="M2 6h12v10H2zM14 10h4l3 3v3h-7z" fill="none" stroke="currentColor" stroke-width="1.8" stroke-linejoin="round"/><circle cx="6" cy="17.5" r="1.8" fill="none" stroke="currentColor" stroke-width="1.6"/><circle cx="17" cy="17.5" r="1.8" fill="none" stroke="currentColor" stroke-width="1.6"/></symbol>
    <symbol id="i-return" viewBox="0 0 24 24"><path d="M5 12a7 7 0 1 0 2-5" fill="none" stroke="currentColor" stroke-width="1.8" stroke-linecap="round"/><path d="M5 3v4h4" fill="none" stroke="currentColor" stroke-width="1.8" stroke-linecap="round" stroke-linejoin="round"/></symbol>
    <symbol id="i-chev" viewBox="0 0 10 10"><path d="M2 3.5l3 3 3-3" fill="none" stroke="currentColor" stroke-width="1.4" stroke-linecap="round"/></symbol>
  </defs>
</svg>

<div class="topbar">
  <span><svg><use href="#i-badge" style="color:#7BADD7"/></svg>Physician-Formulated</span>
  <span><svg><use href="#i-shield"/></svg>&gt;99% Certified Purity</span>
  <span><svg><use href="#i-truck"/></svg>Free UK delivery over £50</span>
</div>

<header class="nav">
  <a class="brand" href="#"><span class="brand-dot"></span>Lunavel</a>
  <nav class="nav-links">
    <a class="active" href="#">Shop</a><a href="#">The Science</a><a href="#">Purity</a><a href="#">About Dr.</a><a href="#">FAQ</a>
  </nav>
  <div class="nav-actions">
    <svg><use href="#i-heart"/></svg>
    <svg><use href="#i-bag"/></svg>
    <a class="btn-primary" href="#">Shop GHK-Cu</a>
  </div>
</header>

<section class="hero">
  <div class="crumbs"><a href="#">Home</a><i>/</i>Shop</div>
  <h1>The Collection</h1>
  <p>Every product is 2% GHK-Cu, surgeon-formulated, and verified above 99% purity by an independent London laboratory.</p>
</section>

<main class="shop">
  <aside class="filters">
    <h3>Category</h3>
    <ul class="cat-list">
      <li class="on">All products</li><li>Face</li><li>Scalp &amp; Hair</li><li>Body</li><li>Serums</li><li>Creams</li><li>Kits</li>
    </ul>
    <div class="divider"></div>
    <h3>Max price</h3>
    <div class="range"></div>
    <div class="range-labels"><span>£40</span><span>Up to <b>£160</b></span></div>
    <div class="divider low"></div>
    <div class="note"><svg style="color:var(--blue)"><use href="#i-badge"/></svg>Every item independently purity-tested</div>
  </aside>

  <section class="results">
    <div class="results-head">
      <div class="count"><b>9</b> products</div>
      <div class="sort">Featured<svg><use href="#i-chev"/></svg></div>
    </div>

    <div class="grid">
      <article class="card">
        <div class="card-media" role="img" aria-label="Product shot of the Renewal Face Serum dropper bottle">
          <span class="pill"><svg><use href="#i-badge"/></svg>Verified</span>
          <span class="ribbon">Bestseller</span>
          <span class="heart"><svg><use href="#i-heart"/></svg></span>
          <span class="product-shot"></span><span class="shadow"></span>
        </div>
        <div class="card-body">
          <div class="card-cat">Face &amp; Fine Lines</div>
          <div class="card-name">Renewal Face Serum</div>
          <div class="card-desc">Daily 2% GHK-Cu serum for firmness and tone · 30 ml</div>
          <div class="card-foot"><span class="price">£68.00</span><span class="add"><svg><use href="#i-cart"/></svg></span></div>
        </div>
      </article>

      <article class="card">
        <div class="card-media" role="img" aria-label="Product shot of the Restorative Face Cream jar">
          <span class="pill"><svg><use href="#i-badge"/></svg>Verified</span>
          <span class="heart"><svg><use href="#i-heart"/></svg></span>
          <span class="product-shot jar"></span><span class="shadow"></span>
        </div>
        <div class="card-body">
          <div class="card-cat">Face &amp; Fine Lines</div>
          <div class="card-name">Restorative Face Cream</div>
          <div class="card-desc">Rich 2% GHK-Cu moisturiser for barrier repair · 50 ml</div>
          <div class="card-foot"><span class="price">£62.00</span><span class="add"><svg><use href="#i-cart"/></svg></span></div>
        </div>
      </article>

      <article class="card">
        <div class="card-media" role="img" aria-label="Product shot of the Scalp and Hair Serum bottle">
          <span class="pill"><svg><use href="#i-badge"/></svg>Verified</span>
          <span class="heart"><svg><use href="#i-heart"/></svg></span>
          <span class="product-shot deep"></span><span class="shadow"></span>
        </div>
        <div class="card-body">
          <div class="card-cat">Scalp &amp; Hair</div>
          <div class="card-name">Scalp &amp; Hair Serum</div>
          <div class="card-desc">Leave-in 2% GHK-Cu for a healthier scalp · 60 ml</div>
          <div class="card-foot"><span class="price">£58.00</span><span class="add"><svg><use href="#i-cart"/></svg></span></div>
        </div>
      </article>

      <article class="card">
        <div class="card-media" role="img" aria-label="Product shot of the Nourishing Head Cream jar">
          <span class="pill"><svg><use href="#i-badge"/></svg>Verified</span>
          <span class="heart"><svg><use href="#i-heart"/></svg></span>
          <span class="product-shot jar"></span><span class="shadow"></span>
        </div>
        <div class="card-body">
          <div class="card-cat">Scalp &amp; Hair</div>
          <div class="card-name">Nourishing Head Cream</div>
          <div class="card-desc">Overnight 2% GHK-Cu scalp treatment mask · 75 ml</div>
          <div class="card-foot"><span class="price">£54.00</span><span class="add"><svg><use href="#i-cart"/></svg></span></div>
        </div>
      </article>

      <article class="card">
        <div class="card-media" role="img" aria-label="Product shot of the Firming Body Lotion pump bottle">
          <span class="pill"><svg><use href="#i-badge"/></svg>Verified</span>
          <span class="heart"><svg><use href="#i-heart"/></svg></span>
          <span class="product-shot"></span><span class="shadow"></span>
        </div>
        <div class="card-body">
          <div class="card-cat">Body &amp; Décolleté</div>
          <div class="card-name">Firming Body Lotion</div>
          <div class="card-desc">Fast-absorbing 2% GHK-Cu for full-body care · 200 ml</div>
          <div class="card-foot"><span class="price">£48.00</span><span class="add"><svg><use href="#i-cart"/></svg></span></div>
        </div>
      </article>

      <article class="card">
        <div class="card-media" role="img" aria-label="Product shot of the Neck and Décolleté Cream jar">
          <span class="pill"><svg><use href="#i-badge"/></svg>Verified</span>
          <span class="heart"><svg><use href="#i-heart"/></svg></span>
          <span class="product-shot jar"></span><span class="shadow"></span>
        </div>
        <div class="card-body">
          <div class="card-cat">Body &amp; Décolleté</div>
          <div class="card-name">Neck &amp; Décolleté Cream</div>
          <div class="card-desc">Targeted 2% GHK-Cu for neck and chest · 50 ml</div>
          <div class="card-foot"><span class="price">£56.00</span><span class="add"><svg><use href="#i-cart"/></svg></span></div>
        </div>
      </article>

      <article class="card">
        <div class="card-media" role="img" aria-label="Product shot of the Eye Renewal Serum bottle">
          <span class="pill"><svg><use href="#i-badge"/></svg>Verified</span>
          <span class="heart"><svg><use href="#i-heart"/></svg></span>
          <span class="product-shot"></span><span class="shadow"></span>
        </div>
        <div class="card-body">
          <div class="card-cat">Face &amp; Fine Lines</div>
          <div class="card-name">Eye Renewal Serum</div>
          <div class="card-desc">Gentle 2% GHK-Cu for the eye area · 15 ml</div>
          <div class="card-foot"><span class="price">£52.00</span><span class="add"><svg><use href="#i-cart"/></svg></span></div>
        </div>
      </article>

      <article class="card">
        <div class="card-media" role="img" aria-label="Product shot of the Post-Procedure Recovery Gel tube">
          <span class="pill"><svg><use href="#i-badge"/></svg>Verified</span>
          <span class="ribbon">Post-procedure</span>
          <span class="heart"><svg><use href="#i-heart"/></svg></span>
          <span class="product-shot"></span><span class="shadow"></span>
        </div>
        <div class="card-body">
          <div class="card-cat">Recovery &amp; Wound Care</div>
          <div class="card-name">Post-Procedure Recovery Gel</div>
          <div class="card-desc">Soothing 2% GHK-Cu gel for skin recovery · 40 ml</div>
          <div class="card-foot"><span class="price">£44.00</span><span class="add"><svg><use href="#i-cart"/></svg></span></div>
        </div>
      </article>

      <article class="card">
        <div class="card-media" role="img" aria-label="Product shot of the three-piece starter kit box">
          <span class="pill"><svg><use href="#i-badge"/></svg>Verified</span>
          <span class="ribbon">Best value</span>
          <span class="heart"><svg><use href="#i-heart"/></svg></span>
          <span class="product-shot kit"></span><span class="shadow"></span>
        </div>
        <div class="card-body">
          <div class="card-cat">Complete Routine</div>
          <div class="card-name">The Complete Ritual — Starter Kit</div>
          <div class="card-desc">Serum + face cream + body lotion, save 20% · 3-piece set</div>
          <div class="card-foot"><span class="price">£148.00</span><span class="add"><svg><use href="#i-cart"/></svg></span></div>
        </div>
      </article>
    </div>
  </section>
</main>

<section class="trust">
  <span><svg><use href="#i-badge"/></svg>&gt;99% verified purity</span>
  <span><svg><use href="#i-truck"/></svg>Free UK delivery over £50</span>
  <span><svg><use href="#i-return"/></svg>30-day returns</span>
  <span><svg><use href="#i-shield"/></svg>Secure checkout</span>
</section>

<footer class="footer">
  <div class="footer-top">
    <div class="footer-brand">
      <a class="brand" href="#"><span class="brand-dot"></span>Lunavel</a>
      <p>Physician-formulated GHK-Cu skincare. Verified purity, clinical standards, published proof.</p>
      <div class="lab"><svg style="color:var(--blue-soft)"><use href="#i-badge"/></svg>Lab Verified · &gt;99% GHK-Cu</div>
    </div>
    <div class="fcol"><h4>SHOP</h4><ul><li>All Products</li><li>Scalp Serum</li><li>Face Serum</li><li>Body Lotion</li><li>Starter Kit</li></ul></div>
    <div class="fcol"><h4>SCIENCE</h4><ul><li>What is GHK-Cu?</li><li>Purity Standards</li><li>Clinical Research</li><li>Lab Reports</li></ul></div>
    <div class="fcol"><h4>COMPANY</h4><ul><li>About Dr. Varenne</li><li>Our Process</li><li>FAQ</li><li>Contact</li></ul></div>
    <div class="fcol"><h4>LEGAL</h4><ul><li>Privacy Policy</li><li>Terms of Service</li><li>Cookie Policy</li><li>Returns</li></ul></div>
  </div>
  <div class="footer-bottom">
    <p>© 2026 Lunavel. Cosmetic product for external use only. Not intended to diagnose, treat, cure or prevent any disease.</p>
    <div class="socials"><span aria-label="Social link"></span><span aria-label="Social link"></span><span aria-label="Social link"></span></div>
  </div>
</footer>

</body>
</html>
```